Global Weight loss program

we need a business card based in Kestrel Bay , OR called PeppertonRUN . Mara Dulvik Tenbrook the founder and creator of PeppertonRUN Movement. A business based around nutrition, health, Whole Foods and fitness.

Industry/Entity Type

Food Service

Contact Information for Business Card

Phone number : 718-555-0143
website www.peppertonrun.com
email : mara@peppertonrun.com

Font styles to use
Sans Serif

Requirements
Must have
• logo colors
• green black and gold
Nice to have
• must be simple and sharp.
Should not have
• pictures of items

```html
<!DOCTYPE html>
<html lang="en">
<head>
<meta charset="utf-8">
<title>PeppertonRUN Business Card</title>
<link href="https://fonts.googleapis.com/css2?family=Dancing+Script:wght@500&family=Open+Sans:wght@400;600&family=Ubuntu:wght@400;700&display=swap" rel="stylesheet">
<style>
  :root {
    --canvas: #ececec;
    --card-green: #4b7232;
    --band-grey: #a3a3a3;
    --ink-dark: #1f2a19;
    --ink-soft: #2c3a24;
    --rule: #6f9253;
    --card-white: #ffffff;
    --band-light-green: #9fcf78;
    --brand-grey: #5f5f5f;
    --brand-green: #7dbb4e;
    --tag-grey: #8a8a8a;
  }
  * { box-sizing: border-box; margin: 0; padding: 0; }
  html, body { width: 1200px; height: 980px; overflow: hidden; }
  body {
    background: var(--canvas);
    font-family: "Open Sans", sans-serif;
    position: relative;
  }
  .card {
    position: absolute;
    top: 340px;
    width: 525px;
    height: 300px;
    box-shadow: 0 6px 18px rgba(0,0,0,0.18);
    overflow: hidden;
  }
  .card--back { left: 45px; background: var(--card-green); }
  .card--front { left: 630px; background: var(--card-white); }

  .band { position: absolute; left: 40px; right: 40px; height: 16px; }
  .card--back .band { background: var(--band-grey); }
  .card--front .band { background: var(--band-light-green); }
  .band--top { top: 0; }
  .band--bottom { bottom: 0; }

  /* contact side */
  .person { position: absolute; left: 70px; top: 46px; }
  .person__name {
    font-family: "Dancing Script", cursive;
    font-size: 31px;
    color: var(--ink-dark);
  }
  .person__role {
    font-family: "Ubuntu", sans-serif;
    font-size: 11px;
    letter-spacing: 0.5px;
    color: var(--ink-soft);
    margin-top: 2px;
    padding-left: 18px;
  }
  .divider {
    position: absolute;
    left: 40px; right: 40px; top: 138px;
    height: 1px;
    background: var(--rule);
  }
  .contacts {
    position: absolute;
    left: 150px; top: 156px;
    list-style: none;
  }
  .contacts li {
    display: flex;
    align-items: center;
    height: 27px;
    font-family: "Ubuntu", sans-serif;
    font-size: 14px;
    color: var(--ink-dark);
  }
  .contacts svg { width: 16px; height: 16px; margin-right: 18px; flex: none; }

  /* brand side */
  .brand-mark {
    position: absolute;
    left: 236px; top: 44px;
    width: 52px; height: 52px;
    background: var(--brand-grey);
  }
  .brand-name {
    position: absolute;
    left: 0; right: 0; top: 116px;
    text-align: center;
    font-family: "Ubuntu", sans-serif;
    font-weight: 700;
    font-size: 40px;
    letter-spacing: 1px;
    text-transform: uppercase;
    color: var(--brand-grey);
  }
  .brand-tagline {
    position: absolute;
    left: 0; right: 0; top: 168px;
    text-align: center;
    font-size: 12px;
    letter-spacing: 2px;
    color: var(--tag-grey);
  }
  .brand-url {
    position: absolute;
    left: 0; right: 0; top: 198px;
    text-align: center;
    font-family: "Ubuntu", sans-serif;
    font-size: 17px;
    color: var(--brand-green);
  }
</style>
</head>
<body>

<section class="card card--back" aria-label="Business card contact side">
  <div class="band band--top"></div>
  <div class="band band--bottom"></div>
  <div class="person">
    <p class="person__name">Mara Dulvik Tenbrook</p>
    <p class="person__role">FOUNDER &amp; CREATOR</p>
  </div>
  <div class="divider"></div>
  <ul class="contacts">
    <li>
      <svg viewBox="0 0 16 16" aria-hidden="true"><path d="M4 1.5l2.3 2.6-1.4 1.8c.8 1.9 2.3 3.4 4.2 4.2l1.8-1.4 2.6 2.3-1.5 2c-5.4-.4-9.6-4.6-10-10z" fill="var(--ink-dark)"/></svg>
      718-555-0143
    </li>
    <li>
      <svg viewBox="0 0 16 16" aria-hidden="true"><rect x="1.5" y="3.5" width="13" height="9" fill="none" stroke="var(--ink-dark)" stroke-width="1.4"/><path d="M1.5 3.5l6.5 5 6.5-5" fill="none" stroke="var(--ink-dark)" stroke-width="1.4"/></svg>
      mara@peppertonrun.com
    </li>
    <li>
      <svg viewBox="0 0 16 16" aria-hidden="true"><circle cx="8" cy="8" r="7" fill="var(--ink-dark)"/><path d="M1.5 8h13M8 1c-3 3.5-3 10.5 0 14M8 1c3 3.5 3 10.5 0 14" fill="none" stroke="var(--card-green)" stroke-width="1"/></svg>
      www.peppertonrun.com
    </li>
    <li>
      <svg viewBox="0 0 16 16" aria-hidden="true"><path d="M8 15s5-5.2 5-8.8A5 5 0 0 0 3 6.2C3 9.8 8 15 8 15z" fill="var(--ink-dark)"/><circle cx="8" cy="6.2" r="1.8" fill="var(--card-green)"/></svg>
      Kestrel Bay , OR
    </li>
  </ul>
</section>

<section class="card card--front" aria-label="Business card brand side">
  <div class="band band--top"></div>
  <div class="band band--bottom"></div>
  <div class="brand-mark" aria-hidden="true"></div>
  <p class="brand-name">PeppertonRUN</p>
  <p class="brand-tagline">Fitness, Nutrition and Health</p>
  <p class="brand-url">www.peppertonrun.com</p>
</section>

</body>
</html>
```